Stationery Design Project

We need a stationery design for our Norwegian trucking company. We have existed for about 15 years and our 12 drivers uses relatively new vehicles to transport goods around in northern Norway. Long distance routes with fresh fish og food transport is our main operations.

We have already made alogo that's printed on our trucks. The logo and a picture of our trucks is attached. I think the logo i crappy, but since its already in use, changing it is not an option in this round. Still using a better colour scheme in the overall stationery and more interesting fonts is possible (altso in the logo).

Company details:
Name: Vikmarka AS
Organisation nr 983 517 608
Post adress: 8640 Brekka

I like minimalism and simplicity. I am avalibly for questions in normal GMT working hours either here or on mail: kjell@brekkafrakt.no

Reason: Hi. Im extending the deadline because I needed some time to find a vector file of our logo. Sorry for the inconvenience

Hi, and thanks for all your interest in the project. Some updates:

-          I have decided to commit to using one of the designs. Some designer will get the payment.

-          I have extended the deadline with 24 hours since I needed some time to find our firms vector logo (a slow Swedish man was holding me up)

-          We will not choose a design before the deadline. No need to rush.

-          We have received a lot of great design and think there is a need to specified the product we want to make:

o   Business Card for all our employers. I just need the design and will duplicate with the correct numbers and name myself. The information on should be: Logo, employer’s name, Phone number, email, website, Postal number and address. Use this as a template: logo, Leif Dahlberg, 47382950, Leif@brekkafrakt.no,, brekkafrakt.no, 8640 Brekka. The order and placement of the information is your creative decision.

o   Stickers to put on the goods we travel. On the sticker the should be the following information: Logo, phone number, Tekst and link: Fraktæ av Vikmarka. Ke du syns? Brekkafrakt.no/tilbakemelding (this means: Handled by Vikmarka. What do you think Brekkafrakt.no/feedback -à the link will be a feedback form). The placement the information and size is your creative decision with some stings: we have been thinking of using Prentolo for printing and see that a size about 6x6 cm, 8x5 or something like that. (with 3000 copies our budget is 200 punds). Any suggestions of other suppliers are welcome. Prentolo price calculator http://www.prentoloprints.example/digital-litho-printing/printing-labels-tags/stickers/

o   Letterhead with logo, address, phone number and organizational number.

o   Envelopes with logo,address, phone number and organizational number.

Have a nice day.

 

 

• Using the blue colour in the logo and using a similar graphic approch.

```html
<!DOCTYPE html>
<html lang="no">
<head>
<meta charset="utf-8">
<title>Vikmarka – Stationery</title>
<link href="https://fonts.googleapis.com/css2?family=Open+Sans:wght@400;600;700&display=swap" rel="stylesheet">
<style>
  :root {
    --navy: #0a1e9c;
    --royal: #1f4fc8;
    --sky: #1a9ee0;
    --sky-pale: #d6ecf7;
    --paper: #f4f4f4;
    --paper-shade: #dcdcdc;
    --ink-grey: #7a7a7a;
    --caption: #8c8c8c;
    --white: #ffffff;
  }
  * { margin: 0; padding: 0; box-sizing: border-box; }
  html, body { width: 1132px; height: 1200px; overflow: hidden; }
  body {
    position: relative;
    font-family: "Open Sans", Arial, sans-serif;
    background: radial-gradient(ellipse at 50% 70%, #ffffff 0%, #fbfbfb 45%, #e9e9e9 100%);
  }
  .sheet {
    position: absolute;
    overflow: hidden;
    background: linear-gradient(90deg, var(--paper-shade) 0%, var(--paper) 22%, #ffffff 55%, var(--paper) 100%);
    box-shadow: 0 6px 8px -4px rgba(0,0,0,0.35);
  }
  .accent-field {
    position: absolute;
    top: 0; right: 0; bottom: 0;
    background: linear-gradient(170deg, rgba(214,236,247,0) 0%, var(--sky-pale) 18%, var(--sky) 55%, var(--royal) 78%, var(--navy) 100%);
  }
  .brand {
    position: absolute;
    display: flex;
    align-items: center;
    color: var(--royal);
    font-weight: 700;
    white-space: nowrap;
  }
  .brand .dot { border-radius: 50%; background: var(--royal); margin-right: 0.35em; }
  .contact {
    position: absolute;
    text-align: right;
    color: var(--white);
    font-style: normal;
    white-space: nowrap;
  }

  .letterhead { left: 459px; top: 184px; width: 595px; height: 841px; }
  .letterhead .accent-field { width: 190px; }
  .letterhead .brand { left: 46px; top: 70px; font-size: 30px; }
  .letterhead .brand .dot { width: 22px; height: 22px; }
  .letterhead .contact { right: 30px; bottom: 32px; font-size: 10px; line-height: 13.3px; }

  .compliment-slip { left: 87px; top: 570px; width: 595px; height: 280px; }
  .compliment-slip .accent-field { width: 240px; }
  .compliment-slip .brand { left: 26px; top: 24px; font-size: 26px; }
  .compliment-slip .brand .dot { width: 18px; height: 18px; }
  .compliment-slip .greeting { position: absolute; left: 30px; top: 214px; font-size: 23px; color: var(--ink-grey); }
  .compliment-slip .contact { right: 20px; bottom: 18px; font-size: 10px; line-height: 13.3px; }

  .business-card { left: 373px; top: 384px; width: 217px; height: 120px; }
  .business-card .accent-field { width: 88px; }
  .business-card .brand { left: 12px; top: 20px; font-size: 14px; }
  .business-card .brand .dot { width: 10px; height: 10px; }
  .business-card .holder { position: absolute; left: 20px; top: 78px; color: var(--ink-grey); }
  .business-card .holder .name { font-size: 8px; }
  .business-card .holder .role { font-size: 4.5px; }
  .business-card .contact { right: 9px; bottom: 6px; font-size: 5.5px; line-height: 9px; }

  .caption { position: absolute; font-size: 10px; color: var(--caption); }
</style>
</head>
<body>

  <section class="sheet letterhead" aria-label="Letterhead">
    <div class="accent-field" role="img" aria-label="Blue sweeping brand graphic"></div>
    <div class="brand"><span class="dot"></span>Vikmarka</div>
    <address class="contact">
      Adress: 8640 Brekka<br>
      Telefon: 983 517 608<br>
      Visit: brekkafrakt.no<br>
      Mail: kjell@brekkafrakt.no
    </address>
  </section>
  <p class="caption" style="left:422px; top:1037px;">Letter Head</p>

  <section class="sheet compliment-slip" aria-label="Compliment slip">
    <div class="accent-field" role="img" aria-label="Blue sweeping brand graphic"></div>
    <div class="brand"><span class="dot"></span>Vikmarka</div>
    <p class="greeting">Med Komplimenter</p>
    <address class="contact">
      Adress: 8640 Brekka<br>
      Telefon: 983 517 608<br>
      Visit: brekkafrakt.no<br>
      Mail: kjell@brekkafrakt.no
    </address>
  </section>
  <p class="caption" style="left:63px; top:861px;">Compliment Slip</p>

  <section class="sheet business-card" aria-label="Business card">
    <div class="accent-field" role="img" aria-label="Blue sweeping brand graphic"></div>
    <div class="brand"><span class="dot"></span>Vikmarka</div>
    <div class="holder">
      <p class="name">Ola Nordvik</p>
      <p class="role">Job Title</p>
    </div>
    <address class="contact">
      A: 8640 Brekka<br>
      T: 983 517 608<br>
      W: brekkafrakt.no<br>
      M: kjell@brekkafrakt.no
    </address>
  </section>
  <p class="caption" style="left:343px; top:521px;">Business Card</p>

</body>
</html>
```